New Greeting Card Design Project

Need a new name on our current business card design and need thank you cards with our logo on them. I need to have a file that I can change the name for future employees or a change in email or phone number. I already have the design but the designer did not give me rights or the ability to change it. I have the logo files.

Font styles to use
Serif

Colors

Designer to choose colors to be used in the design.

```html
<!DOCTYPE html>
<html lang="en">
<head>
<meta charset="utf-8">
<title>Thank You Card</title>
<link rel="stylesheet" href="https://fonts.googleapis.com/css2?family=Caveat+Brush&display=swap">
<style>
  :root {
    --paper: #ffffff;
    --tint: #e3f0fa;
    --navy: #1f3566;
    --sky: #6cb6e8;
    --sun: #e9b322;
    --berry: #c2306e;
    --lime: #b9cf3a;
  }
  html, body {
    margin: 0;
    padding: 0;
    overflow: hidden;
    background: var(--paper);
  }
  .card {
    position: relative;
    width: 1200px;
    height: 706px;
    background: var(--paper);
    overflow: hidden;
    font-family: "Caveat Brush", cursive;
  }
  .pattern {
    position: absolute;
    inset: 0;
    background:
      radial-gradient(circle at 12% 20%, var(--tint) 0, transparent 70px),
      radial-gradient(circle at 30% 14%, var(--tint) 0, transparent 60px),
      radial-gradient(circle at 26% 42%, var(--tint) 0, transparent 65px),
      radial-gradient(circle at 10% 52%, var(--tint) 0, transparent 65px),
      radial-gradient(circle at 11% 82%, var(--tint) 0, transparent 65px),
      radial-gradient(circle at 73% 14%, var(--tint) 0, transparent 60px),
      radial-gradient(circle at 89% 22%, var(--tint) 0, transparent 65px),
      radial-gradient(circle at 73% 40%, var(--tint) 0, transparent 65px),
      radial-gradient(circle at 89% 56%, var(--tint) 0, transparent 65px),
      radial-gradient(circle at 90% 84%, var(--tint) 0, transparent 65px);
  }
  .brand {
    position: absolute;
    left: 0;
    right: 0;
    top: 150px;
    display: flex;
    flex-direction: column;
    align-items: center;
    gap: 22px;
  }
  .brand-dot {
    width: 120px;
    height: 120px;
    border-radius: 50%;
    background: var(--sun);
  }
  .brand-name {
    font-size: 54px;
    color: var(--navy);
    line-height: 1;
  }
  .greeting {
    position: absolute;
    left: 0;
    right: 0;
    top: 430px;
    margin: 0;
    text-align: center;
    font-size: 190px;
    font-weight: 400;
    line-height: 1;
    letter-spacing: 2px;
  }
  .c-sky { color: var(--sky); }
  .c-sun { color: var(--sun); }
  .c-berry { color: var(--berry); }
  .c-lime { color: var(--lime); }
</style>
</head>
<body>
  <main class="card">
    <div class="pattern" role="img" aria-label="Scattered faint light blue puzzle piece pattern"></div>

    <div class="brand">
      <span class="brand-dot"></span>
      <span class="brand-name">Quillbeck Kids Lab</span>
    </div>

    <h1 class="greeting"><span class="c-sky">T</span><span class="c-sun">h</span><span class="c-berry">a</span><span class="c-lime">n</span><span class="c-sky">k</span> <span class="c-sun">Y</span><span class="c-lime">o</span><span class="c-berry">u</span><span class="c-sky">!</span></h1>
  </main>
</body>
</html>
```